I have a small Keystone Co that is growing. I specialize in commercial concrete and custom

I want a site that shows what we do. We specialize in custom deck design and builds. Custom home builds. Commercial concrete . project management

Target Market(s)

Commercial construction companies and custom home builders

Industry/Entity Type

Construction

Number of Pages Required

1 page

Font styles to use
Serif

Colors

Designer to choose colors to be used in the design.

Requirements
Must have
• Pictures and videos of project that we have completed or are in progress

```html
<!DOCTYPE html>
<html lang="en">
<head>
<meta charset="utf-8">
<title>Custom Home Builds — Construction</title>
<link href="https://fonts.googleapis.com/css2?family=Open+Sans:wght@400;600;700;800&display=swap" rel="stylesheet">
<style>
:root{
  --brand:#f4401c;
  --call:#ff7a12;
  --accent:#f5b400;
  --ink:#1d1d1d;
  --text:#555;
  --nav:#3b3b3b;
  --soft:#f5f5f5;
  --line:#e6e6e6;
  --footer:#17191c;
  --footer-bar:#202225;
  --white:#fff;
}
*{margin:0;padding:0;box-sizing:border-box}
html,body{width:1200px;height:2293px;overflow:hidden}
body{font-family:"Open Sans",Arial,sans-serif;color:var(--ink);background:var(--white);position:relative}
.abs{position:absolute}

/* header */
.topbar{position:absolute;left:0;top:0;width:1200px;height:69px;background:var(--white)}
.brand{position:absolute;left:162px;top:20px;display:flex;align-items:center;gap:12px;font-weight:800;font-size:17px;letter-spacing:.3px}
.tagline{position:absolute;left:380px;top:20px;width:430px;text-align:center;font-size:10.5px;font-weight:700;line-height:20px}
.call{position:absolute;left:867px;top:0;width:171px;height:69px;background:var(--call);color:var(--white);text-align:center}
.call small{display:flex;justify-content:center;align-items:center;gap:8px;font-size:10px;font-weight:700;margin-top:15px;letter-spacing:.5px}
.call strong{display:block;font-size:20px;font-weight:600;margin-top:2px}
.mainnav{position:absolute;left:0;top:69px;width:1200px;height:43px;background:var(--nav)}
.mainnav a{position:absolute;top:14px;color:var(--white);text-decoration:none;font-size:10.5px;font-weight:700}
.mainnav a.active{color:var(--accent)}

/* hero */
.hero{position:absolute;left:0;top:112px;width:1200px;height:457px;background:linear-gradient(180deg,#5d6167 0%,#4a4a48 45%,#3d3a34 100%)}
.hero-frame{position:absolute;left:336px;top:114px;width:523px;height:228px;border:1.5px solid rgba(255,255,255,.75)}
.hero-frame::before,.hero-frame::after{content:"";position:absolute;top:60px;width:4px;height:110px;background:transparent}
.hero-title{position:absolute;left:0;top:132px;width:1200px;text-align:center;color:var(--white)}
.hero-title .pre{font-size:33px;letter-spacing:3px;font-weight:400;line-height:40px}
.hero-title h1{font-size:56px;font-weight:800;letter-spacing:3px;line-height:60px}
.hero-title p{font-size:16px;line-height:22px}
.btn{display:inline-block;background:var(--brand);color:var(--white);font-size:11.5px;font-weight:700;text-align:center;text-decoration:none;text-transform:uppercase}
.hero .btn{position:absolute;left:532px;top:270px;width:138px;height:38px;line-height:38px}
.arrow{position:absolute;top:204px;width:30px;height:34px;border:1px solid rgba(255,255,255,.6);background:rgba(0,0,0,.35);display:flex;align-items:center;justify-content:center}

/* services */
.feature{position:absolute;top:634px;width:230px;text-align:center}
.feature h3{font-size:17px;font-weight:600;margin-top:22px}
.feature p{font-size:11.5px;line-height:18.5px;color:var(--text);margin-top:8px}
.feature a{display:block;font-size:10.5px;font-weight:700;color:var(--ink);text-decoration:none;margin-top:12px}

/* projects */
.projects{position:absolute;left:0;top:902px;width:1200px;height:676px;background:var(--soft)}
.section-title{position:absolute;text-align:center;font-size:16px;font-weight:700;letter-spacing:1px}
.section-title::after{content:"";display:block;width:38px;height:3px;background:var(--accent);margin:10px auto 0}
.tile{position:absolute;width:277px;height:191px}
.tile.hover{background:linear-gradient(180deg,#2a3547,#1c2433)}
.tile-overlay{position:absolute;inset:14px;color:var(--white);text-align:center}
.tile-overlay h4{color:var(--accent);font-size:16px;font-weight:400;margin-top:28px}
.tile-overlay p{font-size:11.5px;line-height:18px;margin-top:10px}
.tile-overlay span{display:block;font-size:11px;margin-top:10px}
.corner{position:absolute;width:22px;height:22px;border-color:rgba(255,255,255,.8);border-style:solid}
.projects .btn{position:absolute;left:537px;top:569px;width:126px;height:38px;line-height:38px}

/* clients & testimonials */
.client{position:absolute;width:127px;height:81px;border:1px solid var(--line);display:flex;align-items:center;justify-content:center;gap:6px;font-size:13px;font-weight:700;color:#6b6b6b}
.client i{width:10px;height:10px;background:#6b6b6b;display:inline-block}
.quote{position:absolute;left:642px;top:1694px;width:396px;height:122px;border:1px solid var(--line);padding:16px 30px 0 30px;font-size:11.5px;line-height:18px;color:var(--text)}
.qmark{position:absolute;font-size:22px;color:#c9c9c9;font-weight:800;line-height:1}
.avatar{position:absolute;left:765px;top:1797px;width:66px;height:66px;border-radius:50%;background:linear-gradient(135deg,#8da6c2,#5f7896);border:3px solid var(--white)}
.person{position:absolute;left:840px;top:1830px;color:var(--brand);font-size:14px;font-weight:600}

/* footer */
.footer{position:absolute;left:0;top:1931px;width:1200px;height:304px;background:var(--footer);color:var(--white)}
.footer h5{font-size:14px;font-weight:600;letter-spacing:.5px}
.footer ul{list-style:none}
.footer li{font-size:11px;line-height:27px}
.contact{display:flex;gap:12px;align-items:flex-start;font-size:11.5px;font-weight:600;line-height:17px}
.newsletter p{font-size:10.5px;font-weight:600;line-height:15px;margin-top:14px}
.field{width:202px;height:29px;background:#2d2f33;border:1px solid #3a3c40;font-size:10.5px;color:#aaa;padding:7px 8px;margin-top:10px}
.submit{width:202px;height:31px;background:var(--brand);display:flex;align-items:center;justify-content:center;gap:7px;font-weight:700;font-size:14px;margin-top:9px}
.bottombar{position:absolute;left:0;top:2235px;width:1200px;height:58px;background:var(--footer-bar);color:#cfcfcf}
.copy{position:absolute;left:162px;top:22px;font-size:11.5px}
.copy b{color:var(--white);font-weight:600}
.social{position:absolute;top:4px;width:50px;height:50px;border-radius:50%;background:#0c0d0f}
</style>
</head>
<body>

<header class="topbar">
  <div class="brand">
    <svg width="32" height="28" viewBox="0 0 32 28"><path d="M16 2 2 14h4v12h8v-8h4v8h8V14h4z" fill="var(--brand)"/></svg>
    COMPANY LOGO
  </div>
  <div class="tagline">SPECIALIZE IN CUSTOM DECK DESIGN AND BUILDS. CUSTOM HOME BUILDS.<br>COMMERCIAL CONCRETE . PROJECT MANAGEMENT</div>
  <div class="call">
    <small><svg width="11" height="11" viewBox="0 0 24 24"><path d="M6.6 10.8a15 15 0 0 0 6.6 6.6l2.2-2.2c.3-.3.7-.4 1-.2 1.1.4 2.3.6 3.6.6.6 0 1 .4 1 1V20c0 .6-.4 1-1 1A17 17 0 0 1 3 4c0-.6.4-1 1-1h3.5c.6 0 1 .4 1 1 0 1.3.2 2.5.6 3.6.1.3 0 .7-.2 1z" fill="#fff"/></svg>CALL NOW</small>
    <strong>555-014-2290</strong>
  </div>
</header>

<nav class="mainnav">
  <a class="active" style="left:367px">HOME</a>
  <a style="left:431px">ABOUT US</a>
  <a style="left:518px">SERVICES</a>
  <a style="left:597px">PROJECTS</a>
  <a style="left:680px">PORTFOLIO</a>
  <a style="left:775px">CONTACT US</a>
</nav>

<section class="hero" role="img" aria-label="Photo of a large new home under construction with work vans and lumber in the driveway">
  <div class="hero-frame"></div>
  <div class="hero-title">
    <div class="pre">WE BUILD</div>
    <h1>FUTURES</h1>
    <p>Lorem ipsum dolor sit amet consectetur</p>
  </div>
  <a class="btn" href="#">Read More</a>
  <div class="arrow" style="left:54px"><svg width="8" height="10" viewBox="0 0 8 10"><path d="M6 1 2 5l4 4" stroke="#fff" stroke-width="1.6" fill="none"/></svg></div>
  <div class="arrow" style="left:1104px"><svg width="8" height="10" viewBox="0 0 8 10"><path d="m2 1 4 4-4 4" stroke="#fff" stroke-width="1.6" fill="none"/></svg></div>
</section>

<section>
  <div class="feature" style="left:140px">
    <svg width="68" height="62" viewBox="0 0 68 62"><rect x="4" y="20" width="34" height="26" rx="3" fill="var(--brand)"/><path d="M38 26h14l10 10v10H38z" fill="var(--brand)"/><rect x="44" y="29" width="8" height="7" fill="#fff"/><circle cx="16" cy="50" r="6" fill="var(--brand)" stroke="#fff" stroke-width="2"/><circle cx="50" cy="50" r="6" fill="var(--brand)" stroke="#fff" stroke-width="2"/><path d="M10 6h20l4 14H6z" fill="var(--brand)"/></svg>
    <h3>Commercial Concrete</h3>
    <p>Lorem ipsum dolor sit amet,<br>consectetur adipiscing elit, sed do<br>eiusmod tempor incididunt ut labore<br>et dolore magna aliqua.</p>
    <a href="#">Read More</a>
  </div>
  <div class="feature" style="left:483px">
    <svg width="68" height="62" viewBox="0 0 68 62"><circle cx="40" cy="12" r="6" fill="var(--brand)"/><path d="M30 32c0-8 4-12 10-12s10 4 10 12z" fill="var(--brand)"/><circle cx="20" cy="40" r="7" fill="none" stroke="var(--brand)" stroke-width="5" stroke-dasharray="3 2"/><path d="M14 22a22 22 0 0 1 12-12M54 40a22 22 0 0 1-12 14" stroke="var(--brand)" stroke-width="3" fill="none"/><path d="m24 8 3 3-4 2zM44 56l-3-4 5-1z" fill="var(--brand)"/></svg>
    <h3>Project Management</h3>
    <p>Lorem ipsum dolor sit amet,<br>consectetur adipiscing elit, sed do<br>eiusmod tempor incididunt ut labore<br>et dolore magna aliqua.</p>
    <a href="#">Read More</a>
  </div>
  <div class="feature" style="left:822px">
    <svg width="68" height="62" viewBox="0 0 68 62"><circle cx="22" cy="16" r="8" fill="var(--brand)"/><rect x="19" y="24" width="6" height="5" fill="var(--brand)"/><path d="M22 2v-2M10 6 8 4M34 6l2-2M6 16H3M38 16h3" stroke="var(--brand)" stroke-width="2.4"/><circle cx="46" cy="28" r="6" fill="var(--brand)"/><path d="M36 46c0-7 4-10 10-10s10 3 10 10z" fill="var(--brand)"/><rect x="6" y="46" width="56" height="6" fill="var(--brand)"/></svg>
    <h3>Good Planning</h3>
    <p>Lorem ipsum dolor sit amet,<br>consectetur adipiscing elit, sed do<br>eiusmod tempor incididunt ut labore<br>et dolore magna aliqua.</p>
    <a href="#">Read More</a>
  </div>
</section>

<section class="projects">
  <h2 class="section-title" style="left:0;top:62px;width:1200px">RECENT PROJECTS</h2>
  <div class="tile" style="left:162px;top:133px;background:linear-gradient(180deg,#6a9ad0 0%,#a9c4de 50%,#8a7a5c 70%,#6e6048 100%)" role="img" aria-label="Excavation site with machinery and yellow formwork under a blue sky"></div>
  <div class="tile" style="left:462px;top:133px;background:linear-gradient(180deg,#d8d8d8 0%,#b98457 40%,#a0693f 80%,#d9d9d9 100%)" role="img" aria-label="Timber-framed front porch entrance of a custom home"></div>
  <div class="tile" style="left:761px;top:133px;background:linear-gradient(180deg,#b6bcc4 0%,#cfd3d8 40%,#6d6452 70%,#4f4636 100%)" role="img" aria-label="Graded ground being prepared for a concrete pour"></div>
  <div class="tile" style="left:162px;top:348px;background:linear-gradient(180deg,#bcd0e4 0%,#e8e8e4 45%,#9a8f78 75%,#6b6150 100%)" role="img" aria-label="Small home under construction with stacked building materials"></div>
  <div class="tile hover" style="left:462px;top:348px" role="img" aria-label="Completed home at dusk">
    <span class="corner" style="left:8px;top:8px;border-width:1px 0 0 1px"></span>
    <span class="corner" style="right:8px;top:8px;border-width:1px 1px 0 0"></span>
    <span class="corner" style="left:8px;bottom:8px;border-width:0 0 1px 1px"></span>
    <span class="corner" style="right:8px;bottom:8px;border-width:0 1px 1px 0"></span>
    <div class="tile-overlay">
      <h4>Lorem ipsum</h4>
      <p>Lorem ipsum dolor sit amet,<br>consectetur adipiscing elit, sed<br>do eiusmod tempor</p>
      <span>Read More</span>
    </div>
  </div>
  <div class="tile" style="left:761px;top:348px;background:linear-gradient(135deg,#8d949c 0%,#d7d9db 45%,#c9a640 70%,#9aa0a6 100%)" role="img" aria-label="Aerial view of a concrete building frame with formwork"></div>
  <a class="btn" href="#">View All</a>
</section>

<section>
  <h2 class="section-title" style="left:162px;top:1634px;width:398px">OUR CLIENTS</h2>
  <div class="client" style="left:162px;top:1694px"><i></i>Ridgeway</div>
  <div class="client" style="left:297px;top:1694px"><i></i>Stonefield</div>
  <div class="client" style="left:432px;top:1694px"><i></i>Keystone Co</div>
  <div class="client" style="left:162px;top:1784px"><i></i>Harbor Builders</div>
  <div class="client" style="left:297px;top:1784px"><i></i>Northgate</div>
  <div class="client" style="left:432px;top:1784px"><i></i>Ironline</div>

  <h2 class="section-title" style="left:642px;top:1634px;width:396px">TESTIMONIALS</h2>
  <div class="quote">
    <span class="qmark" style="left:8px;top:8px">“</span>
    Lorem ipsum dolor sit amet, consectetur adipiscing elit, sed do eiusmod tempor incididunt ut labore et dolore magna aliqua. Ut enim ad minim veniam, quis nostrud exercitation ullamco laboris nisi ut aliquip ex ea commodo consequat. Duis aute.
    <span class="qmark" style="right:8px;top:100px">”</span>
  </div>
  <div class="avatar" role="img" aria-label="Client portrait"></div>
  <div class="person">Daniel Brooks</div>
</section>

<footer class="footer">
  <div class="abs" style="left:160px;top:64px;display:flex;align-items:center;gap:12px;font-weight:800;font-size:16px">
    <svg width="32" height="28" viewBox="0 0 32 28"><path d="M16 2 2 14h4v12h8v-8h4v8h8V14h4z" fill="var(--brand)"/></svg>
    COMPANY LOGO
  </div>
  <div class="contact abs" style="left:162px;top:128px">
    <svg width="16" height="16" viewBox="0 0 32 28"><path d="M16 2 2 14h4v12h8v-8h4v8h8V14h4z" fill="var(--brand)"/></svg>
    <span>418 Alder Row,<br>Suite 210 Fairview, OR 97024</span>
  </div>
  <div class="contact abs" style="left:162px;top:186px">
    <svg width="15" height="12" viewBox="0 0 15 12"><rect width="15" height="12" rx="1" fill="var(--brand)"/><path d="m1 1 6.5 5L14 1" stroke="#17191c" stroke-width="1.4" fill="none"/></svg>
    <span>hello@ridgebuild.example</span>
  </div>
  <div class="contact abs" style="left:162px;top:218px;font-size:15px">
    <svg width="14" height="14" viewBox="0 0 24 24"><path d="M6.6 10.8a15 15 0 0 0 6.6 6.6l2.2-2.2c.3-.3.7-.4 1-.2 1.1.4 2.3.6 3.6.6.6 0 1 .4 1 1V20c0 .6-.4 1-1 1A17 17 0 0 1 3 4c0-.6.4-1 1-1h3.5c.6 0 1 .4 1 1 0 1.3.2 2.5.6 3.6.1.3 0 .7-.2 1z" fill="var(--brand)"/></svg>
    <span>555.014.2290</span>
  </div>

  <div class="abs" style="left:439px;top:62px">
    <h5>NAVIGATION</h5>
    <ul style="margin-top:2px"><li>Home</li><li>About Us</li><li>Services</li><li>Projects</li><li>Portfolio</li><li>Contact us</li></ul>
  </div>
  <div class="abs" style="left:611px;top:62px">
    <h5>SERVICES</h5>
    <ul style="margin-top:2px"><li>Custom deck design</li><li>Builds custom deck</li><li>Custom home builds</li><li>Commercial concrete</li><li>Project management</li></ul>
  </div>
  <div class="abs newsletter" style="left:836px;top:62px">
    <h5>NEWSLETTER SUBSCRIBE</h5>
    <p>Subcribe for all news from us. Please<br>enter your email to form below.</p>
    <div class="field">Email address......</div>
    <div class="submit"><svg width="14" height="14" viewBox="0 0 24 24"><path d="M22 2 2 10l7 3 2 8 3-5 5 4z" fill="#fff"/></svg>SUBMIT</div>
  </div>
</footer>

<div class="bottombar">
  <div class="copy">©2018 <b>Custom home builds</b>. All rights reserve.</div>
  <span class="social" style="left:834px" aria-label="Social link"></span>
  <span class="social" style="left:886px" aria-label="Social link"></span>
  <span class="social" style="left:938px" aria-label="Social link"></span>
  <span class="social" style="left:992px" aria-label="Social link"></span>
</div>

</body>
</html>
```